Powerpoint Design for business and consulting company - Brennig-Tautz

I am searching a design specialist who can help me to create a PowerPoint Design for my company. I'm in the business coaching and consulting industry.

The PPT master should be easy to use and include professional formatting (using the fonts of my website). In general, the slide master should have the look and feel of my website (in terms of fonts, colors, logos, possibility to place big photographs, having text and graph slides as well as photo slides with just 1 key message).

The PowerPoint design should fit my cooperate Identity (please see my website https://brennig-tautz.de).
My logos are attached.

Additional information:
- wide screen format - 16: 9
- right set up of a fitting color scheme
https: // tintrow. io / f6ded1-bfcbce-807f84-9cd3d1-666666
# 666666 (Dim Gray) - body / heading text
# 807F84 (Gray Web)
#BFCBCE (Silver Sand) - link hover
# 9cd3d1 (Powder Blue) - Link color
# F6DED1 (Champagne Pink)

- creation of chart templates, using chart tools, and different chart types etc.
- creation of different slide layouts to place content, pictures (in different sizes), optionally Media
- set up of display guide lines
- as well as standard elements, such as text boxes, lines, default shapes, etc.

• Powerpoint Design needs to have:
https://tintrow.io/f6ded1-bfcbce-807f84-9cd3d1-666666
# 807F84 (Gray Web)
# F6DED1 (Champagne Pink)

```html
<!DOCTYPE html>
<html lang="en">
<head>
<meta charset="utf-8">
<title>Service – Greta Brennig-Tautz</title>
<link rel="stylesheet" href="https://fonts.googleapis.com/css2?family=Merriweather:wght@700&family=Source+Sans+3:wght@300;400&family=Noto+Sans:wght@400&display=swap">
<style>
  :root {
    --champagne: #f6ded1;
    --champagne-deep: #e8d3c6;
    --silver: #bfcbce;
    --silver-deep: #b2bec1;
    --gray-web: #807f84;
    --gray-web-deep: #707074;
    --powder: #9cd3d1;
    --powder-deep: #93c5c3;
    --dim: #666666;
    --ink: #333333;
    --text: #444444;
    --guide: #c8c8c8;
    --paper: #ffffff;
  }
  * { margin: 0; padding: 0; box-sizing: border-box; }
  html, body { width: 1200px; height: 674px; overflow: hidden; background: var(--paper); }
  .slide { position: relative; width: 1200px; height: 674px; overflow: hidden; background: var(--paper); }

  .slide-title {
    position: absolute; left: 110px; top: 62px;
    font-family: "Merriweather", Georgia, serif; font-weight: 700;
    font-size: 20px; letter-spacing: 1.6px; color: var(--ink);
  }
  .brand {
    position: absolute; right: 96px; top: 62px;
    display: flex; align-items: center; gap: 10px;
    font-family: "Source Sans 3", Arial, sans-serif; font-weight: 400;
    font-size: 18px; line-height: 22px; color: var(--dim);
    white-space: nowrap;
  }
  .brand__mark { width: 12px; height: 12px; background: var(--powder); }
  .lead {
    position: absolute; left: 0; width: 1194px; top: 147px; text-align: center;
    font-family: "Source Sans 3", Arial, sans-serif; font-weight: 300;
    font-size: 23px; color: var(--text);
  }

  .chart { position: absolute; left: 0; top: 0; width: 1200px; height: 674px; }

  .service { position: absolute; width: 220px; color: var(--text); }
  .service--left { right: 846px; text-align: right; }
  .service--right { left: 854px; text-align: left; }
  .service--top { top: 251px; }
  .service--bottom { top: 407px; }
  .service__name {
    font-family: "Source Sans 3", Arial, sans-serif; font-weight: 300;
    font-size: 17.5px; line-height: 20.5px; color: var(--ink);
  }
  .service__text {
    margin-top: 6px;
    font-family: "Noto Sans", Arial, sans-serif; font-weight: 400; font-size: 10px;
    line-height: 13.5px; letter-spacing: 0.4px; color: #555555;
  }

  .palette { position: absolute; left: 0; bottom: 0; width: 1200px; height: 9px; display: flex; }
  .palette span { flex: 1; }
  .palette .c1 { background: var(--champagne); }
  .palette .c2 { background: var(--silver); }
  .palette .c3 { background: var(--gray-web); }
  .palette .c4 { background: var(--powder); }
  .palette .c5 { background: var(--dim); }
</style>
</head>
<body>
<main class="slide">
  <h1 class="slide-title">SERVICE</h1>
  <div class="brand"><span class="brand__mark" aria-hidden="true"></span>Greta Brennig-Tautz</div>
  <p class="lead">enim accusantium laudantium laudantium sunt perspiciatis</p>

  <svg class="chart" viewBox="0 0 1280 720" aria-hidden="true">
    <g class="guides" fill="none" stroke="var(--guide)" stroke-width="1.5" stroke-dasharray="6 5">
      <polyline points="606,249 418,249 383,312"/>
      <polyline points="455,414 418,479 378,479"/>
      <polyline points="889,309 853,373 815,373"/>
      <polyline points="975,540 938,604 735,604"/>
    </g>
    <g class="wheel">
      <path d="M637,435 L509,307 A181,181 0 0 1 765,307 Z" fill="var(--champagne-deep)"/>
      <path d="M637,435 L765,307 A181,181 0 0 1 765,563 Z" fill="var(--powder-deep)"/>
      <path d="M637,435 L765,563 A181,181 0 0 1 509,563 Z" fill="var(--gray-web-deep)"/>
      <path d="M637,435 L509,563 A181,181 0 0 1 509,307 Z" fill="var(--silver-deep)"/>
      <path d="M637,435 L524,322 A160,160 0 0 1 750,322 Z" fill="var(--champagne)"/>
      <path d="M637,435 L750,322 A160,160 0 0 1 750,548 Z" fill="var(--powder)"/>
      <path d="M637,435 L750,548 A160,160 0 0 1 524,548 Z" fill="var(--gray-web)"/>
      <path d="M637,435 L524,548 A160,160 0 0 1 524,322 Z" fill="var(--silver)"/>
    </g>
    <g class="icons" fill="none" stroke="var(--ink)" stroke-width="2" stroke-linejoin="round">
      <path d="M615,315 H645 L654,324 V354 H615 Z"/>
      <path d="M624,315 V329 H642 V315"/>
      <path d="M624,354 V338 H645 V354"/>
      <path d="M628,344 H641 M628,349 H641"/>
      <rect x="514" y="421" width="50" height="38"/>
      <path d="M528,421 V415 H550 V421"/>
      <path d="M514,436 H564"/>
      <rect x="535" y="430" width="8" height="12" rx="2"/>
      <path d="M709,415 H762"/>
      <rect x="713" y="416" width="45" height="35"/>
      <path d="M735,451 V459 M724,459 H746"/>
      <rect x="719" y="423" width="12" height="10"/>
      <path d="M736,424 H751 M736,430 H751 M719,438 H751 M719,444 H751"/>
      <path d="M615,508 H650 V531 H630 L620,540 V531 H615 Z"/>
      <path d="M650,518 H660 V543 H655 V551 L646,543 H632 V531"/>
      <g fill="var(--ink)" stroke="none">
        <circle cx="625" cy="520" r="2"/><circle cx="632" cy="520" r="2"/><circle cx="639" cy="520" r="2"/>
      </g>
    </g>
  </svg>

  <section class="service service--left service--top">
    <h2 class="service__name">Aspernatur<br>Magni Aperiam</h2>
    <p class="service__text">Lorem ipsum dolor sit amet,<br>consectetur adipiscing.</p>
  </section>
  <section class="service service--left service--bottom">
    <h2 class="service__name">Veritatis Beatae<br>Eos Voluptas</h2>
    <p class="service__text">Lorem ipsum dolor sit amet,<br>consectetur adipiscing.</p>
  </section>
  <section class="service service--right service--top">
    <h2 class="service__name">Doloremque<br>Perspiciatis Natus</h2>
    <p class="service__text">Lorem ipsum dolor sit amet,<br>consectetur adipiscing.</p>
  </section>
  <section class="service service--right service--bottom">
    <h2 class="service__name">Eaque Inventore<br>Consequuntur</h2>
    <p class="service__text">Lorem ipsum dolor sit amet,<br>consectetur adipiscing.</p>
  </section>

  <div class="palette" aria-hidden="true">
    <span class="c1"></span><span class="c2"></span><span class="c3"></span><span class="c4"></span><span class="c5"></span>
  </div>
</main>
</body>
</html>
```